Quirky Label Design for an Exciting UK-Based Organic Skincare Company!

We need label designs across our range of products, we are a high quality yet quirky organic skincare company called Gently Lumora, we use frosted glass packaging, and we are just wanting one design done for now, but the winning designer we would want to work with to design the rest of the labels for us. We also want them to design business cards and other literature at some point and maybe even a website page.

Our label design will go on a 63mm tall frosted glass jar which is 62mm in diameter. The actual label dimensions should be, 170 mm (W) x 50 mm (H). The idea is so that it wraps around the whole jar with the design at one side (at the front) and the ingredients on another (at the back).

LABEL 1
Organic Polynesian Whipped Body Butter
Vanilla Bean
120ml

Made with Organic Shea and Cocoa Butters and exotic Monoi de Tahiti

Ingredients (INCI): Organic Raw Shea Butter (Butyrospermum Parkii), Organic Raw Cocoa Butter (Theobroma Cacao), Monoi de Tahiti (Coconut (Cocos nucifera) oil (and) Tiare (Gardenia tahitensis) flower), Organic Sweet Almond Oil (Prunus Amygdalus Dulcis), Organic Madagascan Vanilla Extract (Vanillin)

Handmade by Gently Lumora Ltd
14 Quillfield Lane, Bournemouth BH2 9RT, UK
Batch:

OPTIONAL WRITING (if it fits in):
100% Natural and Organic
Intensely Moisturising

LABEL 2
Mango Smoothie
120ml

Ingredients (INCI): Organic Raw Shea Butter (Butyrospermum Parkii), Organic Raw Cocoa Butter (Theobroma Cacao), Monoi de Tahiti (Coconut (Cocos nucifera) oil (and) Tiare (Gardenia tahitensis) flower), Organic Sweet Almond Oil (Prunus Amygdalus Dulcis), Organic Mango Flavour (Aroma)

Batch:

100% Natural and Organic
Intensely Moisturising

I have attached a picture of the jar we use and the lid we use for these products, as well as our logo. I've also attached a 'Handmade in Dorset' stamp which we'd like to go on there if possible, along with a shelf life symbol.

I am thinking the background colour of the labels will be either white or even brown paper colour. Perhaps it would be interesting to see it in both. UPDATE: We have decided on white background now, not brown.

The final design should denote handmade, organic, high quality, pure, yet quirky and original / unique. I am thinking perhaps a seemingly hand-drawn black leaf outline? Could fit the bill, but as I say, up to you. Something that says handmade yet professional.

I'd like to have the original Photoshop files from the winning designer so we can use them as a template for the rest of our horizontal labels.

Target Market(s)

Everyone that appreciates a good quality skincare product focusing on natural & organic. Price is mid-range to high

Industry/Entity Type

It Company

Requirements
Must have
• Must make the product look high quality & organic yet quirky and accessible. Must have our logo and the shelf life symbol and the writing as above.
Nice to have
• Nice to have the 'handmade' stamp attached, but not absolutely necessary if it doesn't fit within your design.

```html
<!DOCTYPE html>
<html lang="en">
<head>
<meta charset="utf-8">
<title>Gently Lumora – Whipped Body Butter Labels</title>
<link rel="stylesheet" href="https://fonts.googleapis.com/css2?family=Montserrat:wght@400;500;600&family=Kaushan+Script&display=swap">
<style>
  :root{
    --backdrop:#d1d2d4;
    --paper:#ffffff;
    --ink:#1a1a1a;
    --vanilla-light:#f3e3b8;
    --vanilla-dark:#3b2a22;
    --mango-red:#e0452c;
    --mango-yellow:#f2b233;
    --mango-green:#6a9b3a;
  }
  *{box-sizing:border-box;margin:0;padding:0}
  html,body{width:1200px;height:960px;overflow:hidden;background:var(--backdrop)}
  body{position:relative;font-family:"Montserrat",sans-serif;color:var(--ink)}

  .label{position:absolute;left:22px;width:1156px;height:340px;background:var(--paper)}
  .label--vanilla{top:118px}
  .label--mango{top:502px}

  .brand-name{position:absolute;left:478px;top:22px;width:200px;text-align:center;
    font-family:"Montserrat",sans-serif;font-weight:600;font-size:22px;line-height:25px;letter-spacing:2px;color:var(--ink)}

  .product-title{position:absolute;left:378px;top:97px;width:400px;text-align:center;
    font-weight:400;font-size:22.5px;line-height:32px;letter-spacing:.3px}

  .product-art{position:absolute;top:164px;height:58px}
  .label--vanilla .product-art{left:522px;width:112px;border-radius:30px;
    background:linear-gradient(90deg,var(--vanilla-dark),var(--vanilla-light) 45%,var(--vanilla-light) 55%,var(--vanilla-dark))}
  .label--mango .product-art{left:546px;width:64px;border-radius:50%;
    background:linear-gradient(160deg,var(--mango-red),var(--mango-yellow) 60%,var(--mango-green))}

  .scent-name{position:absolute;left:378px;top:216px;width:400px;text-align:center;
    font-family:"Kaushan Script",cursive;font-size:25px;line-height:36px}

  .product-claim{position:absolute;left:378px;top:273px;width:400px;text-align:center;
    font-size:11px;line-height:14.5px}

  .volume{position:absolute;left:528px;top:310px;width:100px;text-align:center;
    font-family:"Kaushan Script",cursive;font-size:14px;line-height:20px}

  .back-panel{position:absolute;left:22px;top:26px;height:280px;width:172px;
    writing-mode:vertical-rl;text-align:center}
  .back-panel__headline{font-family:"Kaushan Script",cursive;font-size:23px;line-height:36px}
  .back-panel__heading{font-size:11px;line-height:14.5px;margin-right:6px}
  .back-panel__ingredients{font-size:11px;line-height:14.5px}

  .handmade-badge{position:absolute;left:965px;top:141px;width:58px;height:58px;
    border:2px solid var(--ink);border-radius:50%}

  .maker-details{position:absolute;left:1040px;top:66px;height:208px;width:80px;
    writing-mode:vertical-rl;transform:rotate(180deg);text-align:center;font-size:11px;line-height:14.5px}
  .batch{position:absolute;left:1097px;top:150px;height:40px;
    writing-mode:vertical-rl;transform:rotate(180deg);font-size:11px;line-height:14px}
</style>
</head>
<body>

<section class="label label--vanilla">
  <div class="back-panel">
    <p class="back-panel__headline">100% Natural &amp; Organic<br>Intensely Moisturising</p>
    <p class="back-panel__heading">INGREDIENTS (INCI):</p>
    <p class="back-panel__ingredients">Organic Raw Shea Butter (Butyrospermum Parkii),<br>Organic Raw Cocoa Butter (Theobroma Cacao),<br>Monoi de Tahiti (Coconut [Cocos nucifera] oil<br>[and] Tiare [Gardenia tahitensis] flower), Organic<br>Sweet Almond Oil (Prunus Amygdalus Dulcis),<br>Organic Madagascan Vanilla Extract (Vanillin)</p>
  </div>

  <p class="brand-name">GENTLY<br>LUMORA</p>
  <h1 class="product-title">ORGANIC POLYNESIAN<br>WHIPPED BODY BUTTER</h1>
  <div class="product-art" role="img" aria-label="Watercolour vanilla flower with vanilla pods"></div>
  <h2 class="scent-name">Vanilla Bean</h2>
  <p class="product-claim">Made with Organic Shea, Cocoa Butters<br>and exotic Monoi de Tahiti</p>
  <p class="volume">120 ml</p>

  <div class="handmade-badge" role="img" aria-label="Handmade stamp"></div>
  <p class="maker-details">Handmade by Gently Lumora Ltd<br>14 Quillfield Lane,<br>Bournemouth BH2 9RT, UK</p>
  <p class="batch">Batch:</p>
</section>

<section class="label label--mango">
  <div class="back-panel">
    <p class="back-panel__headline">100% Natural &amp; Organic<br>Intensely Moisturising</p>
    <p class="back-panel__heading">INGREDIENTS (INCI):</p>
    <p class="back-panel__ingredients">Organic Raw Shea Butter (Butyrospermum Parkii),<br>Organic Raw Cocoa Butter (Theobroma Cacao),<br>Monoi de Tahiti (Coconut [Cocos nucifera] oil<br>[and] Tiare [Gardenia tahitensis] flower), Organic<br>Sweet Almond Oil (Prunus Amygdalus Dulcis),<br>Organic Madagascan Vanilla Extract (Vanillin)</p>
  </div>

  <p class="brand-name">GENTLY<br>LUMORA</p>
  <h1 class="product-title">ORGANIC POLYNESIAN<br>WHIPPED BODY BUTTER</h1>
  <div class="product-art" role="img" aria-label="Watercolour ripe mango"></div>
  <h2 class="scent-name">Mango Smoothie</h2>
  <p class="product-claim">Made with Organic Shea, Cocoa Butters<br>and exotic Monoi de Tahiti</p>
  <p class="volume">120 ml</p>

  <div class="handmade-badge" role="img" aria-label="Handmade stamp"></div>
  <p class="maker-details">Handmade by Gently Lumora Ltd<br>14 Quillfield Lane,<br>Bournemouth BH2 9RT, UK</p>
  <p class="batch">Batch:</p>
</section>

</body>
</html>
```